Non fiction book cover. The book advises how to get a new job.

The book size will be 20cm high by 13cm wide and I need a front cover which can wrap around to the back. This book has a serious message, but I've tried to make it quite light to read and accessible. So I don't want a cover that is too dour or serious and not frivolous either. At the end of the project, I will need a high resolution 3D image of the book, included as part of the package.<br/>The Title of the book is:- "Past Your Prime? Hunting for the Next Role?<br/>by Gerald Whitcombe-Prynne".<br/>I am thinking of a light yellow background, with a striking image to attract attention. The image and words should be clear and sharp.<br/>Here is the, BACK COVER wording.<br/>"This book tells you clearly and simply the steps that you need to take, to get a job, once you’re over 50.<br/>It advises you on the techniques to use to write a killer CV.<br/>It explains how to ensure that your CV attention.<br/>It shows the best way to approach your local job agency.<br/>It demonstrates the best way to use your network.<br/><br/>This book, written by someone with 30 years’ experience in the recruitment industry, gives you ALL the answers.<br/>Whether you are a top executive or someone after some local part time work, then this book is for you. <br/>With the help of this book you will secure your next position.<br/>

Target Market(s)

UK, over 50s, male and female.

Font styles to use
Serif

Colors
fbee3e

Requirements
Must have
• A clear uncluttered cover.
Should not have
• Fussy and over complicated

```html
<!DOCTYPE html>
<html lang="en">
<head>
<meta charset="utf-8">
<title>Past Your Prime? Hunting for the Next Role? — Cover Wrap</title>
<link rel="stylesheet" href="https://fonts.googleapis.com/css2?family=Antonio:wght@600;700&family=Anton&family=Archivo+Black&family=Jost:wght@600&family=Open+Sans:wght@400&display=swap">
<style>
  :root {
    --page: #ffffff;
    --cover-light: #fdf7cf;
    --cover-mid: #fcf0a4;
    --cover-edge: #fbe67a;
    --ink: #07141f;
    --accent-red: #8c0a05;
    --figure-tone: #1b1a4a;
    --ladder-tone: #6b3a12;
    --blank: #ffffff;
    --body-ink: #1c1c1c;
  }
  * { margin: 0; padding: 0; box-sizing: border-box; }
  html, body { width: 800px; height: 1200px; overflow: hidden; background: var(--page); }

  .canvas { position: relative; width: 800px; height: 1200px; }

  .cover-wrap {
    position: absolute; left: 20px; top: 308px; width: 760px; height: 584px;
    background: radial-gradient(ellipse at 50% 50%, var(--cover-light) 0%, var(--cover-mid) 55%, var(--cover-edge) 100%);
    box-shadow: 0 6px 10px rgba(0,0,0,0.35);
  }

  .title-block { position: absolute; display: block; overflow: visible; }
  .title-block .big { font-family: "Antonio", "Arial Narrow", sans-serif; font-weight: 700; fill: var(--ink); }
  .title-block .red { font-family: "Anton", "Impact", sans-serif; fill: var(--accent-red); }
  .title-block .spaced { font-family: "Archivo Black", "Arial Black", sans-serif; fill: var(--ink); }

  .back-title { left: 131px; top: 59px; width: 97px; height: 135px; }
  .front-title { left: 475px; top: 59px; width: 205px; height: 285px; }

  .back-blurb {
    position: absolute; left: 55px; top: 209px; width: 256px;
    font-family: "Open Sans", sans-serif; font-size: 8.6px; line-height: 12.3px;
    color: var(--body-ink); text-align: justify;
  }

  .author-photo-slot { position: absolute; left: 55px; top: 359px; width: 74px; height: 99px; background: var(--blank); }

  .author-bio { position: absolute; left: 144px; top: 358px; width: 163px; }
  .author-bio h2 {
    font-family: "Jost", sans-serif; font-weight: 600; font-size: 8.2px;
    color: var(--ink); text-transform: uppercase; margin-bottom: 2px;
  }
  .author-bio p {
    font-family: "Open Sans", sans-serif; font-size: 6.6px; line-height: 9.9px;
    color: var(--body-ink); text-align: justify;
  }

  .code-slot { position: absolute; left: 242px; top: 537px; width: 65px; height: 19px; background: var(--blank); }

  .spine-title {
    position: absolute; left: 371px; top: 59px; height: 330px;
    writing-mode: vertical-rl;
    font-family: "Antonio", "Arial Narrow", sans-serif; font-weight: 700;
    font-size: 17px; line-height: 1; color: var(--ink); white-space: nowrap;
  }
  .spine-title .red { color: var(--accent-red); font-family: "Anton", sans-serif; font-weight: 400; }

  .spine-author {
    position: absolute; left: 375px; top: 433px;
    writing-mode: vertical-rl;
    font-family: "Jost", sans-serif; font-weight: 600; font-size: 9.5px;
    color: var(--ink); text-transform: uppercase; white-space: nowrap;
  }

  .climber-illustration {
    position: absolute; left: 475px; top: 302px; width: 58px; height: 222px;
    background: linear-gradient(180deg, var(--figure-tone) 0%, var(--figure-tone) 70%, var(--ladder-tone) 100%);
    opacity: 0.9;
  }

  .front-author {
    position: absolute; left: 475px; top: 540px; width: 205px;
    font-family: "Jost", sans-serif; font-weight: 600; font-size: 15.2px;
    color: var(--ink); text-transform: uppercase; white-space: nowrap; text-align: center;
  }
</style>
</head>
<body>
<div class="canvas">
  <div class="cover-wrap">

    <!-- back cover -->
    <svg class="title-block back-title" viewBox="0 0 205 285" aria-label="Past Your Prime? Hunting for the Next Role?">
      <text class="big" x="0" y="58" font-size="72" textLength="205" lengthAdjust="spacingAndGlyphs">PAST YOUR</text>
      <text class="big" x="0" y="122" font-size="72" textLength="205" lengthAdjust="spacingAndGlyphs">PRIME?</text>
      <text class="red" x="0" y="164" font-size="44" textLength="205" lengthAdjust="spacingAndGlyphs">HUNTING</text>
      <text class="spaced" x="0" y="190" font-size="22" textLength="205" lengthAdjust="spacing">FOR THE</text>
      <text class="red" x="0" y="234" font-size="42" textLength="76" lengthAdjust="spacingAndGlyphs">NEXT</text>
      <text class="big" x="82" y="282" font-size="98" textLength="123" lengthAdjust="spacingAndGlyphs">ROLE?</text>
    </svg>

    <p class="back-blurb">This book tells you clearly and simply the steps that you need to take, to get a job, once you’re over 50. It advises you on the techniques to use to write a killer CV. It explains how to ensure that your CV attention. It shows the best way to approach your local job agency. It demonstrates the best way to use your network. This book, written by someone with 30 years’ experience in the recruitment industry, gives you ALL the answers. Whether you are a top executive or someone after some local part time work, then this book is for you. With the help of this book you will secure your next position.</p>

    <div class="author-photo-slot"></div>
    <div class="author-bio">
      <h2>Gerald Whitcombe-Prynne</h2>
      <p>Lorem Ipsum is simply dummy text of the printing and typesetting industry. Lorem Ipsum has been the industry's standard dummy text ever since the 1500s, when an unknown printer took a galley of type and scrambled it to make a type specimen book. It has survived not only five centuries, but also the leap into electronic typesetting, remaining essentially unchanged.</p>
    </div>
    <div class="code-slot"></div>

    <!-- spine -->
    <div class="spine-title">PAST YOUR PRIME? <span class="red">HUNTING</span> FOR THE <span class="red">NEXT</span> ROLE?</div>
    <div class="spine-author">Gerald Whitcombe-Prynne</div>

    <!-- front cover -->
    <svg class="title-block front-title" viewBox="0 0 205 285" aria-label="Past Your Prime? Hunting for the Next Role?">
      <text class="big" x="0" y="58" font-size="72" textLength="205" lengthAdjust="spacingAndGlyphs">PAST YOUR</text>
      <text class="big" x="0" y="122" font-size="72" textLength="205" lengthAdjust="spacingAndGlyphs">PRIME?</text>
      <text class="red" x="0" y="164" font-size="44" textLength="205" lengthAdjust="spacingAndGlyphs">HUNTING</text>
      <text class="spaced" x="0" y="190" font-size="22" textLength="205" lengthAdjust="spacing">FOR THE</text>
      <text class="red" x="0" y="234" font-size="42" textLength="76" lengthAdjust="spacingAndGlyphs">NEXT</text>
      <text class="big" x="82" y="282" font-size="98" textLength="123" lengthAdjust="spacingAndGlyphs">ROLE?</text>
    </svg>

    <div class="climber-illustration" role="img" aria-label="Illustration of a man in a dark suit climbing a wooden ladder, reaching up towards the title"></div>

    <div class="front-author">Gerald Whitcombe-Prynne</div>
  </div>
</div>
</body>
</html>
```